Logo for Internal Medicine practice

I want a logo for my Internal Medicine practice, I would like it to be with my name on it which is Lucía Barrenechea Ruiz.

I would like the business card to say the following (it is in Spanish since my practice is in Spanish):

Lucía Barrenechea Ruiz
Medicina Interna
Cel. 5583617204
luciabarrenechearuiz@correovela.mx

Logo Text

Lucía Barrenechea

```html
<!DOCTYPE html>
<html lang="es">
<head>
<meta charset="utf-8">
<title>Lucía Barrenechea Ruiz · Tarjeta de presentación</title>
<link rel="stylesheet" href="https://fonts.googleapis.com/css2?family=Montserrat:wght@700&family=Open+Sans:wght@400&display=swap">
<style>
  :root {
    --backdrop: #e4e4e4;
    --card: #ffffff;
    --teal: #16c6b3;
    --blue: #1b7fd4;
    --ink: #4a4a4a;
  }
  html, body {
    margin: 0;
    width: 1200px;
    height: 802px;
    overflow: hidden;
    background: var(--backdrop);
  }
  .business-card {
    position: absolute;
    left: 100px;
    top: 115px;
    width: 1000px;
    height: 572px;
    background: var(--card);
    box-shadow: 0 10px 30px rgba(0,0,0,0.12);
  }
  .brand {
    position: absolute;
    left: 50px;
    top: 300px;
    width: 320px;
    display: flex;
    align-items: center;
    gap: 12px;
  }
  .brand-mark {
    width: 34px;
    height: 34px;
    flex: none;
    background: var(--teal);
  }
  .brand-name {
    font-family: "Montserrat", sans-serif;
    font-weight: 700;
    font-size: 21px;
    color: var(--teal);
    white-space: nowrap;
  }
  .details {
    position: absolute;
    left: 400px;
    top: 150px;
    right: 0;
  }
  .person-name {
    font-family: "Montserrat", sans-serif;
    font-weight: 700;
    font-size: 28px;
    color: var(--teal);
    text-transform: uppercase;
    margin: 0;
    letter-spacing: 0.5px;
    white-space: nowrap;
  }
  .specialty {
    font-family: "Open Sans", sans-serif;
    font-weight: 400;
    font-size: 24px;
    color: var(--blue);
    margin: 2px 0 0;
    letter-spacing: 0.5px;
  }
  .rule {
    height: 3px;
    background: var(--teal);
    margin: 14px 0 16px;
  }
  .contact-list {
    list-style: none;
    margin: 0;
    padding: 0;
    font-family: "Open Sans", sans-serif;
    font-size: 20px;
    color: var(--ink);
    letter-spacing: 0.4px;
  }
  .contact-list li {
    display: flex;
    align-items: center;
    gap: 14px;
    height: 32px;
    white-space: nowrap;
  }
  .contact-icon {
    width: 16px;
    height: 16px;
    flex: none;
  }
</style>
</head>
<body>
  <div class="business-card">
    <div class="brand">
      <div class="brand-mark"></div>
      <div class="brand-name">Lucía Barrenechea</div>
    </div>

    <div class="details">
      <h1 class="person-name">Lucía Barrenechea Ruiz</h1>
      <p class="specialty">Medicina Interna</p>
      <div class="rule"></div>
      <ul class="contact-list">
        <li>
          <svg class="contact-icon" viewBox="0 0 16 16" aria-hidden="true">
            <rect x="3.5" y="1" width="9" height="14" rx="2" fill="none" stroke="var(--blue)" stroke-width="1.8"/>
            <circle cx="8" cy="12.3" r="0.9" fill="var(--blue)"/>
          </svg>
          5583617204
        </li>
        <li>
          <svg class="contact-icon" viewBox="0 0 16 16" aria-hidden="true">
            <rect x="1" y="3" width="14" height="10" rx="1" fill="var(--blue)"/>
            <path d="M1.5 3.8 L8 9 L14.5 3.8" fill="none" stroke="#fff" stroke-width="1.3"/>
          </svg>
          luciabarrenechearuiz@correovela.mx
        </li>
        <li>
          <svg class="contact-icon" viewBox="0 0 16 16" aria-hidden="true">
            <circle cx="8" cy="8" r="6.5" fill="none" stroke="var(--blue)" stroke-width="1.8"/>
            <path d="M1.5 8 H14.5 M8 1.5 Q4.5 8 8 14.5 M8 1.5 Q11.5 8 8 14.5" fill="none" stroke="var(--blue)" stroke-width="1.2"/>
          </svg>
          barrenecheamedicina.mx
        </li>
      </ul>
    </div>
  </div>
</body>
</html>
```